Website update for Mobile lighting company

We are looking to get a fresh look to our website and update it with some new products and services we are just starting to offer. We host there website through site nest and use there website builder so we would like comparable files. The pages we would want are:
Home page
VEXA (one of our light tower units)
KR62 (one of our light tower units)
KR38 (one of our light tower units)
KR14 (one of our light tower units)
Service Page (would describe different serves we provide)
Contact Page with a google map
We would like to stick with our company colours and keep it clean and modern looking. Current website is www.brindlepowr.ca

```html
<!DOCTYPE html>
<html lang="en">
<head>
<meta charset="utf-8">
<title>Brindle Power Corp. – Lighting Systems for the Future</title>
<link href="https://fonts.googleapis.com/css2?family=Open+Sans:wght@400;600;700&display=swap" rel="stylesheet">
<style>
:root{
  --lime:#b5c21d;
  --ink:#222;
  --navy:#2c3e50;
  --muted:#777;
  --topbar:#161616;
  --footer:#111;
  --card:#eeeeee;
  --slate:#3e4f68;
  --white:#fff;
}
*{margin:0;padding:0;box-sizing:border-box}
html,body{width:901px;height:1200px;overflow:hidden;background:var(--white)}
body{font-family:'Open Sans',Arial,sans-serif;color:var(--ink);position:relative}
.abs{position:absolute}

.topbar{left:0;top:0;width:901px;height:25px;background:var(--topbar)}
.topbar .phone{left:100px;top:6px;font-size:11px;color:#ddd}
.social-top{right:90px;top:0;display:flex;height:25px}
.social-top span{width:26px;height:25px;border-left:1px solid #444;display:flex;align-items:center;justify-content:center}
.social-top span:last-child{border-right:1px solid #444}
.social-top i{width:9px;height:9px;border-radius:50%;background:#fff;display:block}

.header{left:0;top:25px;width:901px;height:65px;background:var(--white);border-bottom:1px solid #e5e5e5}
.brand{left:60px;top:18px;display:flex;align-items:center;gap:10px}
.brand-dot{width:30px;height:30px;border-radius:50%;background:var(--lime)}
.brand-name{font-size:20px;font-weight:700;color:var(--lime);letter-spacing:.5px}
.nav{top:22px;font-size:11px;font-weight:600;color:var(--ink)}
.nav.active{color:var(--lime)}
.search{left:781px;top:17px;width:29px;height:29px}

.hero{left:0;top:90px;width:901px;height:222px;background:linear-gradient(180deg,#3b3f45 0%,#8f9aa6 45%,#c9d1da 75%,#d7dbdf 100%)}

.intro-title{left:0;top:326px;width:901px;text-align:center;font-size:16px;font-weight:600;color:var(--navy);letter-spacing:.3px}
.intro-sub{left:0;top:352px;width:901px;text-align:center;font-size:10px;color:var(--muted)}
.intro-text{left:22px;top:398px;width:857px;text-align:center;font-size:11px;line-height:21px;color:var(--ink)}

.solution{left:0;top:461px;width:901px;height:342px;background:linear-gradient(180deg,#4a5a72 0%,var(--slate) 55%,#34445c 100%)}
.sol-title{left:0;top:537px;width:901px;text-align:center;font-size:16px;font-weight:600;color:var(--white)}
.sol-sub{left:0;top:560px;width:901px;text-align:center;font-size:11px;color:#9aa6b8}
.sol-item{top:607px;width:100px;text-align:center}
.sol-item svg{display:block;margin:0 auto}
.sol-item p{margin-top:6px;font-size:12px;color:#9aa6b8}

.clients-title{left:0;top:827px;width:901px;text-align:center;font-size:18px;font-weight:600;color:var(--navy)}
.clients-sub{left:0;top:854px;width:901px;text-align:center;font-size:9.5px;color:#555}
.card{top:900px;height:118px;background:var(--card);border-top:3px solid var(--lime);padding:12px 8px 0 9px}
.card p{font-size:9.5px;line-height:14px;color:#999}
.card h4{margin-top:8px;font-size:13px;font-weight:400;color:var(--lime)}
.card small{display:block;font-size:8px;color:#999;margin-top:2px}

.footer{left:0;top:1028px;width:901px;height:172px;background:var(--footer)}
.f-col{top:1061px}
.f-col h3{font-size:14px;font-weight:700;color:var(--lime);margin-bottom:10px}
.f-col p{font-size:10px;line-height:14px;color:var(--white)}
.subscribe{display:flex;margin-top:17px}
.subscribe span{width:136px;height:27px;background:var(--white);border-radius:2px;font-size:10px;color:#999;padding:7px 7px}
.subscribe b{width:31px;height:27px;margin-left:4px;background:var(--lime);color:var(--white);font-size:10px;font-weight:400;display:flex;align-items:center;justify-content:center}
.news{display:flex;gap:12px;margin-bottom:7px}
.news i{width:22px;height:22px;border:1px solid #777;background:#3a2a30;flex:none;margin-top:2px}
.news p{font-size:10px;line-height:14px}
.news em{display:block;font-style:normal;font-size:8.5px;color:var(--lime);margin-top:4px}
.addr p{font-size:11px;line-height:16px}
.addr .lbl{color:var(--lime)}
.f-social{display:flex;gap:14px;margin-top:10px}
.f-social i{width:14px;height:14px;border-radius:50%;background:var(--white);display:block}
</style>
</head>
<body>

<div class="abs topbar">
  <div class="abs phone">Call Us Now : 5875550143</div>
  <div class="abs social-top" aria-label="Social links"><span><i></i></span><span><i></i></span><span><i></i></span><span><i></i></span></div>
</div>

<header class="abs header">
  <div class="abs brand"><span class="brand-dot"></span><span class="brand-name">Brindle Power Corp.</span></div>
  <span class="abs nav active" style="left:354px">HOME</span>
  <span class="abs nav" style="left:414px">VEXA</span>
  <span class="abs nav" style="left:471px">KR62</span>
  <span class="abs nav" style="left:527px">KR38</span>
  <span class="abs nav" style="left:582px">KR14</span>
  <span class="abs nav" style="left:637px">SERVICE</span>
  <span class="abs nav" style="left:710px">CONTACT</span>
  <svg class="abs search" viewBox="0 0 29 29" aria-label="Search">
    <circle cx="14.5" cy="14.5" r="13" fill="none" stroke="#2c3e50" stroke-width="2"/>
    <circle cx="13" cy="13" r="5" fill="none" stroke="#2c3e50" stroke-width="2"/>
    <line x1="16.6" y1="16.6" x2="20.5" y2="20.5" stroke="#2c3e50" stroke-width="2.4" stroke-linecap="round"/>
  </svg>
</header>

<div class="abs hero" role="img" aria-label="Photo of an indoor gymnasium with basketball hoops under bright ceiling lights"></div>

<h1 class="abs intro-title">LIGHTING SYSTEMS FOR THE FUTURE</h1>
<p class="abs intro-sub">Brindle Power Corp. has changed the way the drilling industry sees, literally.</p>
<p class="abs intro-text">The VEXA RIDGE MOUNT lighting system (patent pending) combines a sophisticated, yet obvious design with the latest technology to bring not only a safer solution for illumination but an environmentally beneficial solution as well.</p>

<section class="abs solution" role="img" aria-label="Faded photo of a waterfront city skyline under a blue overlay"></section>
<h2 class="abs sol-title">OUR SOLUTION</h2>
<p class="abs sol-sub">Loreum Ipsum Loreum Ipsum Loreum Ipsum</p>

<svg width="0" height="0" style="position:absolute">
  <defs>
    <g id="ico-ship" fill="#fff"><rect x="-3" y="-18" width="6" height="5"/><rect x="-8" y="-13" width="16" height="7"/><path d="M-16 -6 H16 L11 5 H-11 Z"/><path d="M-16 9 q4 -3 8 0 t8 0 t8 0 t8 0 v3 q-4 -3 -8 0 t-8 0 t-8 0 t-8 0z"/></g>
    <g id="ico-city" fill="#fff"><rect x="-14" y="-8" width="10" height="24"/><rect x="-3" y="-18" width="10" height="34"/><rect x="8" y="-4" width="8" height="20"/></g>
    <g id="ico-compass"><circle r="15" fill="none" stroke="#fff" stroke-width="3"/><path d="M0 -12 L4 0 L0 12 L-4 0Z M-12 0 L0 -4 L12 0 L0 4Z" fill="#fff"/></g>
  </defs>
</svg>

<div class="abs sol-item" style="left:128px"><svg width="84" height="84" viewBox="-42 -42 84 84"><circle r="40" fill="none" stroke="#fff" stroke-width="2.5"/><use href="#ico-ship"/></svg><p>Loreum Ipsum</p></div>
<div class="abs sol-item" style="left:232px"><svg width="84" height="84" viewBox="-42 -42 84 84"><circle r="40" fill="none" stroke="#fff" stroke-width="2.5"/><use href="#ico-city"/></svg><p>Loreum Ipsum</p></div>
<div class="abs sol-item" style="left:336px"><svg width="84" height="84" viewBox="-42 -42 84 84"><circle r="40" fill="none" stroke="#fff" stroke-width="2.5"/><use href="#ico-ship"/></svg><p>Loreum Ipsum</p></div>
<div class="abs sol-item" style="left:440px"><svg width="84" height="84" viewBox="-42 -42 84 84"><circle r="40" fill="none" stroke="#fff" stroke-width="2.5"/><use href="#ico-compass"/></svg><p>Loreum Ipsum</p></div>
<div class="abs sol-item" style="left:544px"><svg width="84" height="84" viewBox="-42 -42 84 84"><circle r="40" fill="none" stroke="#fff" stroke-width="2.5"/><use href="#ico-city"/></svg><p>Loreum Ipsum</p></div>
<div class="abs sol-item" style="left:647px"><svg width="84" height="84" viewBox="-42 -42 84 84"><circle r="40" fill="none" stroke="#fff" stroke-width="2.5"/><use href="#ico-ship"/></svg><p>Loreum Ipsum</p></div>

<h2 class="abs clients-title">HAPPY CLIENTS</h2>
<p class="abs clients-sub">what customer say about us and why love our services!</p>

<div class="abs card" style="left:0;width:216px"><p>Lorem Ipsum is simply dummy text of the printing and typeset industry. Lorem Ipsum has been the industry's standard dummy text ever hen an with new version look.</p><h4>Client Name</h4><small>United States</small></div>
<div class="abs card" style="left:225px;width:218px"><p>Lorem Ipsum is simply dummy text of the printing and typeset industry. Lorem Ipsum has been the industry's standard dummy text ever hen an with new version look.</p><h4>Client Name</h4><small>United States</small></div>
<div class="abs card" style="left:452px;width:218px"><p>Lorem Ipsum is simply dummy text of the printing and typeset industry. Lorem Ipsum has been the industry's standard dummy text ever hen an with new version look.</p><h4>Client Name</h4><small>United States</small></div>
<div class="abs card" style="left:678px;width:219px"><p>Lorem Ipsum is simply dummy text of the printing and typeset industry. Lorem Ipsum has been the industry's standard dummy text ever hen an with new version look.</p><h4>Client Name</h4><small>United States</small></div>

<footer class="abs footer"></footer>
<div class="abs f-col" style="left:90px;width:170px">
  <h3>News letter</h3>
  <p>Duis autem vel eum iriure dolor in hendrerit in vulputate velit esse molestie consequat, vel illum dolore.</p>
  <div class="subscribe"><span>Subscribes..</span><b>GO</b></div>
</div>
<div class="abs f-col" style="left:273px;width:170px">
  <h3>Latest News</h3>
  <div class="news"><i></i><p>Postformat Gallery: Multiple images<em>December 12, 2012 - 9:11 pm</em></p></div>
  <div class="news"><i></i><p>Postformat Gallery: Multiple images<em>December 12, 2012 - 9:11 pm</em></p></div>
</div>
<div class="abs f-col" style="left:458px;width:172px">
  <h3>Challenge:</h3>
  <p>Traditional location lighting requires multiple light towers throughout a location, gallons of diesel and can be labour intensive. Find out how VEXA RIDGE MOUNT solves many of the challenges of conventional light towers.</p>
</div>
<div class="abs f-col addr" style="left:641px;width:220px">
  <h3>Address</h3>
  <p>#4, 18 Ridgeview Lane NE</p>
  <p>Calder, Alberta T0K 3M2</p>
  <p class="lbl">E-mail:</p>
  <p>info@brindlepowr.ca</p>
  <div class="f-social" aria-label="Social links"><i></i><i></i><i></i><i></i></div>
</div>

</body>
</html>
```